political campaign lawn sign - Governor's Council in Massachuesetts

We are looking for a political lawn sign. We are running a campaign for Governor's Council in Massachusetts. This sign will be on the lawn of homes and businesses so people driving by will see it. It needs to be simple and bold. The last name is long so maybe it could say vote for Marty and then Kolbeck will be big a bold on the next line??
We need it to say:
Vote for Martin Kolbeck
Governor's Council.

Target Market(s)

local residents

Industry/Entity Type

Politcal Campaign

Font styles to use
Sans Serif
Other font styles liked:
• not sure what font but a modern looking one such as Helvetica, Arial, Sans Seri, sharp sans..

Colors
0054AA
0677BA
7BADD7
CADEEF
E8F1F8
00AB8E
00BBA5
67D7C9
C6EFE9
E9F9F6
FFF300
FFF600
FEFA6F
FFFEC7
FFFEE8

Requirements
Must have
• My name written out with a Capital D and R but lower case for every other letter so its Marty Kolbeck
Nice to have
• modern font , the Colors of the lawn sign should have Blue, Yellow and White something bold that will stand out
Should not have
• any maps of Massachusetts

```html
<!DOCTYPE html>
<html lang="en">
<head>
<meta charset="utf-8">
<title>Vote for Marty Kolbeck – Governor Council Lawn Sign</title>
<link rel="stylesheet" href="https://fonts.googleapis.com/css2?family=Russo+One&family=Roboto+Condensed:wght@800&family=Roboto:wght@900&display=swap">
<style>
  :root {
    --backdrop: #e6e9ee;
    --sign-yellow: #fff300;
    --sign-blue: #17329a;
    --sign-navy: #0b1d5a;
    --sign-white: #ffffff;
  }
  html, body {
    margin: 0;
    width: 1200px;
    height: 800px;
    overflow: hidden;
    background: var(--backdrop);
  }
  .lawn-sign {
    position: absolute;
    left: 80px;
    top: 10px;
    width: 1040px;
    height: 780px;
    display: flex;
    flex-direction: column;
    box-shadow: 0 6px 18px rgba(0,0,0,0.18);
  }
  .header-band {
    height: 193px;
    background: var(--sign-yellow);
    display: flex;
    align-items: center;
    justify-content: center;
  }
  .header-band h2 {
    margin: 0;
    font-family: "Russo One", sans-serif;
    font-weight: 400;
    font-size: 128px;
    letter-spacing: 10px;
    color: var(--sign-navy);
    line-height: 1;
  }
  .candidate-panel {
    position: relative;
    height: 477px;
    background: var(--sign-blue);
  }
  .star-row {
    position: absolute;
    top: 30px;
    display: flex;
    gap: 20px;
  }
  .star-row--left { left: 36px; }
  .star-row--right { right: 36px; }
  .star-row svg { width: 50px; height: 48px; }
  .candidate-name {
    position: absolute;
    left: 0;
    right: 0;
    margin: 0;
    text-align: center;
    font-family: "Roboto Condensed", "Roboto", sans-serif;
    font-weight: 800;
    font-size: 164px;
    line-height: 1;
    color: var(--sign-white);
    text-shadow: -7px 7px 0 var(--sign-navy);
  }
  .candidate-name--first { top: 22px; }
  .candidate-name--last { top: 206px; }
  .office-title {
    position: absolute;
    left: 0;
    right: 0;
    top: 394px;
    margin: 0;
    text-align: center;
    font-family: "Russo One", sans-serif;
    font-weight: 400;
    font-size: 70px;
    line-height: 1;
    color: var(--sign-yellow);
  }
  .website-band {
    height: 110px;
    background: var(--sign-navy);
    display: flex;
    align-items: center;
    justify-content: center;
    font-family: "Roboto", sans-serif;
    font-weight: 900;
    font-size: 66px;
    color: var(--sign-white);
  }
</style>
</head>
<body>
  <main class="lawn-sign">
    <div class="header-band"><h2>VOTE FOR</h2></div>
    <section class="candidate-panel">
      <div class="star-row star-row--left" aria-hidden="true">
        <svg viewBox="0 0 24 23"><polygon fill="#fff300" points="12,0 15,8.5 24,8.7 17,14.2 19.5,23 12,17.8 4.5,23 7,14.2 0,8.7 9,8.5"/></svg>
        <svg viewBox="0 0 24 23"><polygon fill="#fff300" points="12,0 15,8.5 24,8.7 17,14.2 19.5,23 12,17.8 4.5,23 7,14.2 0,8.7 9,8.5"/></svg>
        <svg viewBox="0 0 24 23"><polygon fill="#fff300" points="12,0 15,8.5 24,8.7 17,14.2 19.5,23 12,17.8 4.5,23 7,14.2 0,8.7 9,8.5"/></svg>
      </div>
      <div class="star-row star-row--right" aria-hidden="true">
        <svg viewBox="0 0 24 23"><polygon fill="#fff300" points="12,0 15,8.5 24,8.7 17,14.2 19.5,23 12,17.8 4.5,23 7,14.2 0,8.7 9,8.5"/></svg>
        <svg viewBox="0 0 24 23"><polygon fill="#fff300" points="12,0 15,8.5 24,8.7 17,14.2 19.5,23 12,17.8 4.5,23 7,14.2 0,8.7 9,8.5"/></svg>
        <svg viewBox="0 0 24 23"><polygon fill="#fff300" points="12,0 15,8.5 24,8.7 17,14.2 19.5,23 12,17.8 4.5,23 7,14.2 0,8.7 9,8.5"/></svg>
      </div>
      <h1 class="candidate-name candidate-name--first">Marty</h1>
      <p class="candidate-name candidate-name--last">Kolbeck</p>
      <p class="office-title">GOVERNOR COUNCIL</p>
    </section>
    <footer class="website-band">voteformartyk.org</footer>
  </main>
</body>
</html>
```